Etiketten für Gummibärchenglas
Zielgruppe
Wir sind Arbeitgeber für Pflegeberufe und bieten Arbeitsmodelle, die den Pflegeberuf erträglicher gestalten die Mitarbeiter entlasten und besser bezahlen!
Aufgabenstellung
Unseren Bewerbern sagen wir immer....'bevor Sie sich entscheiden hören Sie auf Ihr Bauchgefühl...! ' Wenn dieses komische Signale sendet, lassen Sie lieber die Finger davon!'
Nun haben wir uns überlegt, unseren Bewerbern zum Abschied aus dem Vorstellungsgespräch ein kleines 'Einmachglas' als Geschenk mitzugeben wo nur grüne Gummibärchen darin sind und ein super ansprechenden Etikett darauf ist mit einem Satz wie z.B.: K7-VITANOR....für ein gutes Bauchgefühl.
Dieses Etikett soll selbstverständlich optisch hochwertig, witzig oder ansprechend sein. Idealerweise alles zusammen! ;)
Unsere Logos/Farben und sonstiges finden Sie unter www.dienstwerk-9.de oder auf unserer Facebook-Seite: https://www.sozialnetz-beispiel.de/DienstwerkNeun/?ref=bookmarks
hier sind die Gläser die etikettiert werden sollen: https://www.kaufhafen-online.de/dp/X00Q41ZTRA/ref=kh_5172093_296851202_QX_item

```html
<!DOCTYPE html>
<html lang="de">
<head>
<meta charset="utf-8">
<title>Etikett – Für ein gutes Bauchgefühl</title>
<link href="https://fonts.googleapis.com/css2?family=Playfair+Display:wght@900&display=swap" rel="stylesheet">
<style>
  :root {
    --page: #ffffff;
    --label-green: #049b3b;
    --figure-green: #0f8a3a;
    --figure-shade: #0c7434;
    --disc-green: #127a3b;
    --text-white: #ffffff;
  }
  html, body {
    margin: 0;
    padding: 0;
    width: 1200px;
    height: 1200px;
    overflow: hidden;
    background: var(--page);
  }
  .canvas {
    position: relative;
    width: 1200px;
    height: 1200px;
    background: var(--page);
  }
  .label {
    position: absolute;
    left: 80px;
    top: 80px;
    width: 1040px;
    height: 1040px;
    background: var(--label-green);
    overflow: hidden;
  }
  .label-disc {
    position: absolute;
    left: 450px;
    top: 410px;
    width: 580px;
    height: 580px;
    border-radius: 50%;
    background: var(--disc-green);
    opacity: 0.7;
  }
  .label-figure {
    position: absolute;
    left: 500px;
    top: 0;
    width: 520px;
    height: 1040px;
    background: linear-gradient(180deg, var(--figure-green) 0%, var(--figure-shade) 100%);
    opacity: 0.45;
    border-radius: 240px 240px 0 0;
  }
  .label-headline {
    position: absolute;
    left: 66px;
    top: 268px;
    margin: 0;
    font-family: "Playfair Display", Georgia, serif;
    font-weight: 900;
    font-size: 138px;
    line-height: 155px;
    letter-spacing: -1px;
    color: var(--text-white);
  }
  .brand-name {
    position: absolute;
    left: 670px;
    top: 548px;
    font-family: "Playfair Display", Georgia, serif;
    font-weight: 900;
    font-size: 34px;
    line-height: 1;
    color: var(--text-white);
    white-space: nowrap;
  }
</style>
</head>
<body>
  <main class="canvas">
    <section class="label">
      <div class="label-disc"></div>
      <div class="label-figure" role="img" aria-label="Gezeichnete Frau in Top und kurzer Hose, die Hände auf dem Bauch, in Grüntönen"></div>
      <h1 class="label-headline">Für ein<br>gutes<br>Bauch-<br>gefühl.</h1>
      <span class="brand-name">K7-VITANOR</span>
    </section>
  </main>
</body>
</html>
```